Local electrical company needs two flyers designed

We are a small local electrical contracting company and are in desperate need of a awasome flyer design to help grow our business

hi everyone.

please keep the logo off the front page.
it can go on the rear.

We are really trying to portray a angry/frustrated women BECAUSE her lights are broken.
not light globes

Target Market(s)

Home owners

Industry/Entity Type

Electrical

Font styles to use
Serif

Requirements
Nice to have

```html
<!DOCTYPE html>
<html lang="en">
<head>
<meta charset="utf-8">
<title>Bright Spark Electrical – Flyer</title>
<link rel="stylesheet" href="https://fonts.googleapis.com/css2?family=Oswald:wght@600;700&family=Open+Sans:ital,wght@0,700;0,800;1,700&display=swap">
<style>
  :root{
    --page:#ffffff;
    --black:#000000;
    --band:#4a4a4a;
    --white:#ffffff;
    --cream:#f6f4e2;
    --cream-deep:#e9e6c8;
    --green:#1b8a3a;
    --green-panel:#1f8c3f;
    --green-light:#6cbf4a;
    --orange:#e07a22;
    --red:#d42b20;
    --navy:#1e2a3a;
    --tan:#e8c9a0;
  }
  *{margin:0;padding:0;box-sizing:border-box}
  html,body{width:848px;height:1200px;overflow:hidden;background:var(--page)}
  body{position:relative;font-family:"Open Sans",Arial,sans-serif}

  .card{position:absolute;left:24px;width:802px;height:567px;overflow:hidden}
  .card--front{top:19px;background:var(--black)}
  .card--back{top:614px;background:linear-gradient(180deg,var(--cream) 0%,var(--cream) 55%,var(--cream-deep) 100%)}

  /* front */
  .hero-photo{position:absolute;left:246px;top:0;width:324px;height:425px;
    background:radial-gradient(ellipse at 50% 72%,#c46a1c 0%,#6a3510 28%,#1a0d05 55%,#000 80%)}
  .headline-band{position:absolute;left:0;top:446px;width:100%;height:89px;background:var(--band);
    color:var(--white);text-align:center;font-weight:800}
  .headline-band__lead{font-size:22px;margin-top:10px;line-height:28px}
  .headline-band__main{font-size:35px;line-height:44px;letter-spacing:.5px}

  /* back */
  .call-now{position:absolute;left:26px;top:36px;font-family:"Oswald",Impact,sans-serif;font-weight:700;
    font-size:46px;line-height:1;letter-spacing:-.5px;paint-order:stroke fill;-webkit-text-stroke:6px var(--white);
    text-shadow:2px 3px 3px rgba(0,0,0,.35)}
  .call-now__label{color:var(--green)}
  .call-now__phone{color:var(--orange);margin-left:6px}

  .benefits{position:absolute;left:24px;top:98px;list-style:none}
  .benefits li{display:flex;align-items:center;height:38px;font-size:18px;font-weight:700;color:var(--green)}
  .benefits svg{width:36px;height:32px;margin-right:8px;flex:none}

  .payment-cards{position:absolute;left:282px;top:205px;display:flex;gap:8px}
  .payment-card{width:58px;height:36px;border-radius:4px;background:var(--white);border:1px solid #b9b9b9;
    display:flex;align-items:center;justify-content:center;font-size:11px;font-weight:700;color:var(--green)}

  .mascot-art{position:absolute;left:470px;top:20px;width:322px;height:196px;border-radius:8px;
    background:linear-gradient(135deg,var(--tan) 0%,#d9e6c6 55%,#bfe0f2 100%)}
  .brand-name{position:absolute;left:486px;top:226px;font-family:"Oswald",Impact,sans-serif;font-weight:700;
    font-size:28px;color:var(--orange);line-height:1}

  .orange-rule{position:absolute;left:0;top:256px;width:478px;height:19px;background:var(--orange)}
  .offer-panel{position:absolute;left:0;top:275px;width:478px;height:292px;background:var(--green-panel)}
  .divider{position:absolute;left:0;top:256px}

  .offer-title{position:absolute;left:30px;top:284px;font-family:"Oswald",Impact,sans-serif;font-weight:700;
    font-size:108px;line-height:1;color:var(--green-light);paint-order:stroke fill;-webkit-text-stroke:8px var(--white);
    text-shadow:3px 4px 4px rgba(0,0,0,.45)}
  .offer-sub{position:absolute;left:36px;top:400px;font-family:"Oswald",Impact,sans-serif;font-weight:600;
    font-size:27px;line-height:1;color:var(--orange);paint-order:stroke fill;-webkit-text-stroke:5px var(--white)}
  .offer-info{position:absolute;left:70px;top:442px;color:var(--white);font-size:10.5px;font-weight:700;line-height:14px}
  .offer-info__small{font-style:italic}
  .offer-url{position:absolute;left:68px;top:474px;color:var(--white);font-size:21px;font-weight:800}
  .offer-terms{position:absolute;left:70px;top:506px;color:var(--white);font-size:10.5px;font-style:italic;font-weight:700;line-height:14px}

  .testimonial{position:absolute;left:534px;top:318px;width:250px;color:var(--green);font-size:15.5px;
    font-style:italic;font-weight:700;line-height:24px}
  .testimonial__author{margin-top:14px;color:var(--orange);font-size:17px;font-style:normal}
</style>
</head>
<body>

<section class="card card--front">
  <div class="hero-photo" role="img" aria-label="Photo of a hanging light bulb bursting into flame above a burning hundred-dollar bill"></div>
  <div class="headline-band">
    <p class="headline-band__lead">Tired of replacing bulbs? Lights keep flicking off?</p>
    <p class="headline-band__main">Burning a hole in your wallet?</p>
  </div>
</section>

<section class="card card--back">
  <h2 class="call-now"><span class="call-now__label">CALL NOW</span><span class="call-now__phone">1300 555 019</span></h2>

  <ul class="benefits">
    <li><svg viewBox="0 0 36 32"><path d="M4 29 L18 4 L32 29 Z" fill="none" stroke="var(--red)" stroke-width="3" stroke-linejoin="round"/><path d="M11 19 L17 25 L34 6" fill="none" stroke="var(--green)" stroke-width="3.5" stroke-linecap="round"/></svg>Specialising in domestic electrical repairs</li>
    <li><svg viewBox="0 0 36 32"><path d="M4 29 L18 4 L32 29 Z" fill="none" stroke="var(--red)" stroke-width="3" stroke-linejoin="round"/><path d="M11 19 L17 25 L34 6" fill="none" stroke="var(--green)" stroke-width="3.5" stroke-linecap="round"/></svg>On Time guarantee or $100 OFF</li>
    <li><svg viewBox="0 0 36 32"><path d="M4 29 L18 4 L32 29 Z" fill="none" stroke="var(--red)" stroke-width="3" stroke-linejoin="round"/><path d="M11 19 L17 25 L34 6" fill="none" stroke="var(--green)" stroke-width="3.5" stroke-linecap="round"/></svg>Up front pricing</li>
    <li><svg viewBox="0 0 36 32"><path d="M4 29 L18 4 L32 29 Z" fill="none" stroke="var(--red)" stroke-width="3" stroke-linejoin="round"/><path d="M11 19 L17 25 L34 6" fill="none" stroke="var(--green)" stroke-width="3.5" stroke-linecap="round"/></svg>No mess guaranteed</li>
  </ul>

  <div class="payment-cards">
    <span class="payment-card">Cardline</span>
    <span class="payment-card">Paywell</span>
    <span class="payment-card">Tapcard</span>
  </div>

  <div class="mascot-art" role="img" aria-label="Illustration of a caped superhero electrician mascot holding up a light bulb on a bent cord"></div>
  <p class="brand-name">Bright Spark Electrical</p>

  <div class="orange-rule"></div>
  <div class="offer-panel"></div>
  <svg class="divider" width="802" height="311" viewBox="0 0 802 311">
    <polygon points="478,0 492,0 470,311 456,311" fill="var(--navy)"/>
  </svg>

  <p class="offer-title">SAVE $25</p>
  <p class="offer-sub">off every 3rd downlight replaced</p>
  <div class="offer-info">
    <p>For more information visit www.brightsparkelectrical.com.au/led</p>
    <p class="offer-info__small">Replace your old $$$ burning halogen downlights with new money saving led downlights</p>
  </div>
  <p class="offer-url">www.brightsparkelectrical.com.au</p>
  <div class="offer-terms">
    <p>*Mention this offer when you book your job to receive offer.</p>
    <p>&nbsp;Limit one per household</p>
    <p>*Cannot be combined with any other offer</p>
  </div>

  <blockquote class="testimonial">
    <p>“Excellent electrician! Turns up on time, friendly and a can-do attitude. Did several jobs here including installing (and recommending) LED lights in our kitchen and dining room. No mess, quick and efficient. Highly recommended”</p>
    <p class="testimonial__author">R.Hollis Leichhardt</p>
  </blockquote>
</section>

</body>
</html>
```